Kem7Dex Letterhead

Need a new letterhead for my law firm.
IDENTIFYING INFORMATION BELOW:
Ansel T Brightwater III
Attorney at Law
Address: 4832 Tillbury Rd, Ste 250, Dallas, TX 75204
Phone: 866-402-7183
Fax: 469-583-0271
Email: kem@kem7dex.example
Website: www.kem7dex.example

Colors
0054AA
0677BA
7BADD7
CADEEF
E8F1F8

Requirements
Must have
• Logo needs to be on the letterhead, along with identifying information which is included in the project description.

```html
<!DOCTYPE html>
<html lang="en">
<head>
<meta charset="utf-8">
<title>Kem7Dex Letterhead</title>
<link href="https://fonts.googleapis.com/css2?family=Open+Sans:wght@300;400;700;800&display=swap" rel="stylesheet">
<style>
  :root {
    --backdrop: #d6dadb;
    --paper: #ffffff;
    --ink: #111111;
    --ink-soft: #6d6f72;
    --accent-blue: #0677ba;
    --rule: #b9bcbf;
  }
  * { margin: 0; padding: 0; box-sizing: border-box; }
  html, body {
    width: 1200px;
    height: 784px;
    overflow: hidden;
    background: var(--backdrop);
    font-family: "Open Sans", Arial, sans-serif;
  }
  .letterhead {
    position: absolute;
    left: 320px;
    top: 30px;
    width: 560px;
    height: 724px;
    background: var(--paper);
    box-shadow: 0 6px 18px rgba(0,0,0,0.12);
    overflow: hidden;
  }
  .corner-wedge {
    position: absolute;
    display: block;
  }
  .corner-wedge--top { left: 0; top: 0; }
  .corner-wedge--bottom { right: 0; bottom: 0; }
  .brand {
    position: absolute;
    left: 28px;
    top: 44px;
  }
  .brand-name {
    font-weight: 800;
    font-size: 34px;
    letter-spacing: 1px;
    line-height: 1;
    color: var(--ink);
    text-transform: uppercase;
  }
  .brand-tagline {
    margin-top: 4px;
    font-weight: 300;
    font-size: 12.5px;
    letter-spacing: 1.6px;
    color: var(--ink);
    text-transform: uppercase;
  }
  .contact {
    position: absolute;
    right: 26px;
    top: 46px;
    padding-left: 10px;
    border-left: 1px solid var(--rule);
    font-size: 8px;
    line-height: 1.45;
  }
  .contact-line {
    display: flex;
    align-items: center;
    gap: 4px;
    color: var(--ink-soft);
  }
  .contact-icon { width: 7px; height: 7px; flex: none; }
  .contact-address {
    margin-top: 1px;
    font-weight: 700;
    color: var(--ink);
  }
</style>
</head>
<body>
  <main class="letterhead">
    <svg class="corner-wedge corner-wedge--top" width="240" height="40" viewBox="0 0 240 40" aria-hidden="true">
      <polygon points="0,0 240,0 0,40" fill="var(--ink)"/>
    </svg>

    <header class="brand">
      <div class="brand-name">Kem7Dex</div>
      <div class="brand-tagline">Law with momentum</div>
    </header>

    <address class="contact" style="font-style: normal;">
      <div class="contact-line">
        <svg class="contact-icon" viewBox="0 0 10 10" aria-hidden="true"><path d="M2 1h2l1 2.5-1.3 1a6 6 0 0 0 2.8 2.8l1-1.3L10 7v2a1 1 0 0 1-1 1A9 9 0 0 1 1 2a1 1 0 0 1 1-1z" fill="var(--ink)"/></svg>
        <span>866-402-7183</span>
      </div>
      <div class="contact-line">
        <svg class="contact-icon" viewBox="0 0 10 10" aria-hidden="true"><rect x="1" y="3" width="8" height="5" rx="1" fill="var(--ink)"/><rect x="3" y="1" width="4" height="2" fill="var(--ink)"/></svg>
        <span>469-583-0271</span>
      </div>
      <div class="contact-line">
        <svg class="contact-icon" viewBox="0 0 10 10" aria-hidden="true"><rect x="0.5" y="2" width="9" height="6" rx="1" fill="var(--ink)"/><path d="M1 2.5l4 3 4-3" stroke="#fff" stroke-width="0.8" fill="none"/></svg>
        <span>kem@kem7dex.example</span>
      </div>
      <div class="contact-line">
        <svg class="contact-icon" viewBox="0 0 10 10" aria-hidden="true"><circle cx="5" cy="5" r="4.2" fill="none" stroke="var(--ink)" stroke-width="1.2"/><path d="M1 5h8M5 1c-2 2.5-2 5.5 0 8M5 1c2 2.5 2 5.5 0 8" stroke="var(--ink)" stroke-width="0.8" fill="none"/></svg>
        <span>www.kem7dex.example</span>
      </div>
      <div class="contact-address">4832 Tillbury Rd, Ste 250,<br>Dallas, TX 75204</div>
    </address>

    <svg class="corner-wedge corner-wedge--bottom" width="280" height="90" viewBox="0 0 280 90" aria-hidden="true">
      <polygon points="280,0 280,90 0,90" fill="var(--accent-blue)"/>
    </svg>
  </main>
</body>
</html>
```